Web Design Project

We are looking for a beautiful, clean web page design for our new web service: Tavernik. The idea behind tavernik is simple. People tell us where they live and what they love, and we point them towards interesting offers, places and events near them - as reviewed by our experts and their friends. It is available on the web and by phone. We have chosen our logo and know the elements we want on each page. Now we just need a whole a great design to pull it all together.
///
TaVernik
locate, explore and discover the best of your city with tavernik
Discover your cities hottest offers
places & venues while sharing
the things that mean the most to you.
Join for free today!
//
Note: we have also had some feedback that the name is difficult to read/pronounce, so we might want to change the color of the word be in tavernik so that it stands out. suggestions welcome.
Target Market(s)
Young, urban, savvy consumers
We are looking at this site for inspiration
https://strovento.example/
elements: blog:latest news, top picks // members area // categories: fashion & beauty; food & drink; entertainment & events

```html
<!DOCTYPE html>
<html lang="en">
<head>
<meta charset="utf-8">
<title>Tavernik – Advice and resources for anyone planning trips</title>
<link rel="stylesheet" href="https://fonts.googleapis.com/css2?family=Arimo:wght@400;700&family=Montserrat:wght@600;700&family=Questrial&display=swap">
<style>
:root{
  --teal:#137f93;
  --teal-dark:#0c6a7d;
  --teal-text:#1a8aa0;
  --orange:#f4701f;
  --orange-dark:#d85a10;
  --green:#1f8a2b;
  --page:#efefef;
  --white:#ffffff;
  --ink:#222222;
  --muted:#555555;
  --field:#cfe1e5;
  --fb:#3b5a9a;
}
*{box-sizing:border-box;margin:0;padding:0}
html,body{width:872px;height:1200px;overflow:hidden;background:var(--page)}
body{font-family:"Arimo",Arial,sans-serif;color:var(--ink);position:relative}
.abs{position:absolute}
.header-scene{left:0;top:0;width:872px;height:272px;background:linear-gradient(180deg,#1aa3b5 0%,#178fa3 35%,#137f93 100%)}
.header-rocks{left:250px;top:0;width:460px;height:105px;background:radial-gradient(ellipse at 55% 40%,#7a6a52 0%,#5d5444 45%,rgba(23,143,163,0) 75%)}
.header-rule{left:0;top:270px;width:872px;height:7px;background:var(--orange)}
.logo-card{left:28px;top:-8px;width:238px;height:130px;background:var(--white);transform:rotate(-5deg);box-shadow:0 3px 8px rgba(0,0,0,.35)}
.logo{left:70px;top:52px;display:flex;align-items:center;gap:10px;font-family:"Questrial",sans-serif;font-size:27px;color:#4a4a4a}
.logo-dot{width:16px;height:16px;background:#6a2f8f}
.main-nav{left:318px;top:107px;width:515px;height:38px;background:var(--orange);border-radius:4px 4px 0 0;display:flex;align-items:center;justify-content:center;font-size:12.5px;color:var(--white)}
.main-nav a,.foot-nav a{color:inherit;text-decoration:none}
.main-nav span,.foot-nav span{margin:0 8px}
.hero{left:27px;top:145px;width:817px;height:283px;background:var(--white);border-radius:4px;box-shadow:0 2px 6px rgba(0,0,0,.25)}
.hero-panel{left:39px;top:156px;width:794px;height:261px;background:linear-gradient(180deg,#1a8ea3,#0f7488);overflow:hidden}
.hero-kicker{left:22px;top:52px;font-family:"Montserrat",sans-serif;font-weight:600;font-size:18.5px;color:var(--white)}
.hero-title{left:17px;top:76px;font-family:"Montserrat",sans-serif;font-weight:700;font-size:28.5px;color:var(--white);text-shadow:0 2px 3px rgba(0,0,0,.35)}
.hero-sub{left:18px;top:121px;font-size:15px;color:#e8f6f9}
.hero-body{left:18px;top:148px;width:410px;font-size:10.5px;line-height:13px;color:#e8f6f9}
.btn-orange{left:17px;top:193px;width:140px;height:26px;background:var(--orange);border:1px solid #ffb37a;border-radius:3px;color:#222;font-size:12px;display:flex;align-items:center;justify-content:center}
.hero-photo{left:465px;top:7px;width:322px;height:247px;background:linear-gradient(180deg,#b6cfe6 0%,#d9d5c7 35%,#a69b82 55%,#3f5a2d 80%,#6f6a5c 100%)}
.offer-tab{left:252px;top:7px;width:322px;height:247px}
.fb-btn{left:26px;top:444px;width:233px;height:46px;background:var(--fb);border-radius:2px;display:flex;align-items:center;gap:14px;padding-left:14px;color:var(--white);font-weight:700;font-size:17px}
.fb-square{width:19px;height:19px;background:var(--white);opacity:.9}
.cat-band{left:300px;top:444px;width:548px;height:41px}
.cat-text{left:329px;top:455px;font-size:15px;color:var(--white)}
.cat-text b{color:#111}
.content{left:25px;top:504px;width:822px;height:557px;background:var(--white)}
.section-title{font-size:21px;color:var(--teal-text);font-weight:400}
.news-title{left:46px;top:524px}
.news-date{font-size:11px;font-weight:700;color:var(--orange)}
.news-text{width:480px;font-size:10.5px;line-height:12px;color:#222}
.btn-teal{height:26px;background:linear-gradient(180deg,#1b8fa4,#0c6579);border-radius:3px;color:var(--white);font-size:12.5px;display:flex;align-items:center;justify-content:center;box-shadow:0 1px 2px rgba(0,0,0,.4)}
.login{left:555px;top:519px;width:270px;height:207px;border-left:1px dotted #888;border-right:1px dotted #888;background:linear-gradient(90deg,#f3f3f3,#ffffff 20%,#ffffff 80%,#f3f3f3)}
.login-shadow{left:590px;top:722px;width:210px;height:14px;border-radius:50%;background:radial-gradient(ellipse,rgba(0,0,0,.18),rgba(0,0,0,0) 70%)}
.field-label{font-size:13px;color:#111}
.field{width:220px;height:25px;background:var(--field)}
.picks-title{left:46px;top:738px}
.tile{width:181px;height:119px;border:1px solid var(--teal);overflow:hidden}
.tile-label{position:absolute;left:0;top:0;width:100%;height:31px;background:rgba(255,255,255,.78);font-family:"Questrial",sans-serif;font-size:21px;text-align:center;line-height:32px}
.foot-nav{left:27px;top:1082px;font-size:12px;color:#222}
.foot-nav span{margin:0 7px}
.copyright{left:27px;top:1113px;font-size:11px;line-height:16.5px;color:#444}
.foot-logo{left:762px;top:1124px;display:flex;align-items:center;gap:6px;font-family:"Questrial",sans-serif;font-size:17px;color:#9a9a9a}
.foot-dot{width:10px;height:10px;background:#9a9a9a}
</style>
</head>
<body>

<div class="abs header-scene" role="img" aria-label="Coastal cliffs and turquoise sea"></div>
<div class="abs header-rocks" aria-hidden="true"></div>
<div class="abs header-rule"></div>

<div class="abs logo-card"></div>
<div class="abs logo"><span class="logo-dot"></span>tavernik</div>

<nav class="abs main-nav">
  <a href="#">Home</a><span>|</span><a href="#">About</a><span>|</span><a href="#">Blog</a><span>|</span><a href="#">Latest News</a><span>|</span><a href="#">Top Picks</a><span>|</span><a href="#">Members Area</a><span>|</span><a href="#">Categories</a>
</nav>

<div class="abs hero"></div>
<section class="abs hero-panel">
  <svg class="abs" style="left:300px;top:0" width="220" height="70" viewBox="0 0 220 70" aria-hidden="true">
    <polygon points="20,0 60,0 30,30 0,30" fill="var(--orange)"/>
    <polygon points="80,0 130,0 80,50 45,36" fill="var(--green)"/>
    <polygon points="155,0 205,0 150,60 105,45" fill="var(--white)"/>
  </svg>
  <div class="abs hero-kicker">ADVICE AND RESOURCES FOR</div>
  <h1 class="abs hero-title">ANYONE PLANNING TRIPS</h1>
  <p class="abs hero-sub">Helping you making the most of your trip and events</p>
  <p class="abs hero-body">Lorem Ipsum has been the industry's standard dummy text ever since the 1500s, when an unknown printer took a galley of type and scrambled.</p>
  <a class="abs btn-orange">Read More Information</a>
  <div class="abs hero-photo" role="img" aria-label="Ornate royal palace with tiered golden spires and trimmed gardens"></div>
  <svg class="abs" style="left:730px;top:7px" width="57" height="125" viewBox="0 0 57 125" aria-hidden="true">
    <polygon points="15,0 57,0 57,125 0,55" fill="var(--orange)"/>
  </svg>
  <svg class="abs" style="left:740px;top:12px" width="60" height="60" viewBox="0 0 60 60" aria-hidden="true">
    <text transform="translate(8,12) rotate(38)" font-family="Arimo,sans-serif" font-weight="700" font-size="15" fill="#111">Hotest</text>
    <text transform="translate(4,32) rotate(38)" font-family="Arimo,sans-serif" font-weight="700" font-size="15" fill="#111">Offer</text>
  </svg>
</section>

<a class="abs fb-btn"><span class="fb-square"></span>Sign In with Linkbook</a>

<svg class="abs cat-band" viewBox="0 0 548 41" aria-hidden="true">
  <polygon points="18,0 548,0 548,41 17,41 17,33 0,33 17,24" fill="var(--teal)"/>
  <polygon points="515,41 545,2 548,2 548,14 532,41" fill="var(--orange)"/>
  <polygon points="497,41 527,2 537,2 507,41" fill="var(--orange)"/>
</svg>
<p class="abs cat-text"><b>Categories:</b> Fashion &amp; beauty, Food &amp; Drink, Entertainment &amp; Events</p>

<main class="abs content"></main>

<h2 class="abs section-title news-title">Latest News</h2>
<p class="abs news-date" style="left:47px;top:559px">November 22/11</p>
<p class="abs news-text" style="left:47px;top:583px">Lorem ipsum dolor sit amet, consectetur adipiscing elit. Nam luctus luctus ipsum, eget laoreet is faucibus id. Maecenas pretium euismod eros a malesuada.</p>
<p class="abs news-date" style="left:47px;top:618px">November 18/11</p>
<p class="abs news-text" style="left:47px;top:642px">Vestibulum porta blandit sapien sed blandit. Phasellus orci sem, ullamcorper vitae blandit nons faucibus id dui. Nulla pulvinar ultricies arcuis.</p>
<a class="abs btn-teal" style="left:47px;top:682px;width:89px">Read More</a>

<div class="abs login-shadow"></div>
<aside class="abs login">
  <h2 class="abs section-title" style="left:26px;top:14px">Member Login</h2>
  <label class="abs field-label" style="left:26px;top:47px">User Name</label>
  <div class="abs field" style="left:26px;top:64px"></div>
  <label class="abs field-label" style="left:26px;top:100px">Password</label>
  <div class="abs field" style="left:26px;top:117px"></div>
  <a class="abs btn-teal" style="left:26px;top:159px;width:70px">Submit</a>
</aside>

<h2 class="abs section-title picks-title">Top Picks</h2>

<div class="abs tile" style="left:46px;top:779px;background:linear-gradient(180deg,#4a86d6,#3a6ec4 50%,#8a6a5a 85%,#3d5a30)" role="img" aria-label="Oklahoma City skyline"><span class="tile-label" style="color:#111">Oklahoma City</span></div>
<div class="abs tile" style="left:246px;top:779px;background:linear-gradient(180deg,#9ab9d8,#6f8aa6 50%,#b9c7d4 80%,#3e6a3a)" role="img" aria-label="Singapore waterfront skyline with fountain"><span class="tile-label" style="color:var(--green)">Singapore</span></div>
<div class="abs tile" style="left:445px;top:779px;background:linear-gradient(180deg,#dfe9ef,#8fa89a 50%,#4d7a3f 80%,#6a9a3a)" role="img" aria-label="Vienna glasshouse in a park"><span class="tile-label" style="color:var(--orange)">Vienna</span></div>
<div class="abs tile" style="left:645px;top:779px;background:linear-gradient(180deg,#bcd0e6,#8a7a6a 45%,#6a4a3a 75%,#4a3a30)" role="img" aria-label="Baltimore home arts building with sculpture"><span class="tile-label" style="color:var(--teal-text)">Baltimore</span></div>

<div class="abs tile" style="left:46px;top:918px;background:linear-gradient(160deg,#c9c9c9,#d94040 45%,#b82a2a 70%,#1a1a1a)" role="img" aria-label="Las Vegas welcome sign"><span class="tile-label" style="color:#111">Las Vegas</span></div>
<div class="abs tile" style="left:246px;top:918px;background:linear-gradient(180deg,#8aa86a,#b8a07a 45%,#a8786a 70%,#7ab0c8)" role="img" aria-label="River raft ride at a theme park"><span class="tile-label" style="color:#111">Magicland</span></div>
<div class="abs tile" style="left:445px;top:918px;background:linear-gradient(180deg,#c8d8e2,#6f8a8a 40%,#4a6a5a 70%,#9ab8cc)" role="img" aria-label="Texas lake below wooded hills"><span class="tile-label" style="color:#111">Texas</span></div>
<div class="abs tile" style="left:645px;top:918px;background:linear-gradient(180deg,#a8c8e8,#5a6a8a 45%,#3a4a6a 75%,#8a8a8a)" role="img" aria-label="Orlando theme park globe"><span class="tile-label" style="color:#111">Orlando</span></div>

<nav class="abs foot-nav">
  <a href="#">Home</a><span>|</span><a href="#">About</a><span>|</span><a href="#">Blog</a><span>|</span><a href="#">Latest News</a><span>|</span><a href="#">Top Picks</a><span>|</span><a href="#">Members Area</a><span>|</span><a href="#">Categories</a>
</nav>
<p class="abs copyright">© Copyright 2011 Tavernik. All Rights Reserved<br>Website Design &amp; Developed | SEO PPC Services: www.northpixel.example</p>
<div class="abs foot-logo"><span class="foot-dot"></span>tavernik</div>

</body>
</html>
```